Postcard for commercial concrete cleaning company that will be mailed to business customers

A 6x9 postcard that will be mailed out to businesses who have concrete (sidewalks, drive thrus, dumpster pads, etc) that need periodic pressure washing to keep clean. Our current customers are majority restaurants. We are able to remove gum and grease from concrete which is difficult for much of our competitors. We work at night when the businesses are closed or slow if 24hr.

Target Market(s)

This will go to restaurants, banks, gas stations and other retail locations.

Colors

Designer to choose colors to be used in the design.

Requirements
Must have
• Logo. A headline that mentions commercial concrete cleaning so recipients will know at a glance what we do
Nice to have
• The image included is of a fast food doorway that is half cleaned, the right side. Something like "Dirty Doorway?" may make sense.
• We specialize is maintenance concrete cleaning where we come on a regular basis so I like phrase keep your concrete clean, or keep your business clean. something like that.

```html
<!DOCTYPE html>
<html lang="en">
<head>
<meta charset="utf-8">
<title>Riverbend Commercial Pressure Washing – Postcard</title>
<link rel="stylesheet" href="https://fonts.googleapis.com/css2?family=Lato:wght@400;700&family=Ropa+Sans&display=swap">
<style>
  :root{
    --stage:#4f4f4f;
    --navy:#27235f;
    --blue:#1d6aa2;
    --sky:#2d8ad0;
    --band:#3a8fcf;
    --charcoal:#2e2e30;
    --white:#ffffff;
    --stamp:#e6e6e6;
    --ink:#1b1a4a;
  }
  html,body{margin:0;padding:0;width:1200px;height:1200px;overflow:hidden;background:var(--stage);}
  .sheet{position:absolute;left:0;top:0;width:1500px;height:1500px;transform:scale(.8);transform-origin:0 0;font-family:"Lato",sans-serif;}
  .card{position:absolute;overflow:hidden;background:var(--white);}
  .card--front{left:124px;top:179px;width:862px;height:575px;}
  .card--back{left:522px;top:816px;width:874px;height:582px;}
  .card svg.shapes{position:absolute;left:0;top:0;}
  .t{position:absolute;white-space:nowrap;}
  .brand-name{font-weight:700;color:var(--navy);font-size:27px;letter-spacing:.5px;transform:translateX(-50%);}
  .brand-tag{font-size:19px;letter-spacing:5px;color:var(--navy);transform:translateX(-50%);}
  .headline{font-family:"Ropa Sans",sans-serif;color:var(--white);transform:translateX(-50%);line-height:1;}
  .body-copy{color:var(--white);font-size:18px;line-height:22.5px;white-space:normal;text-align:justify;}
  .section-title{color:var(--white);font-weight:700;font-size:24px;}
  .section-title::after{content:"";display:inline-block;width:98px;height:2px;background:var(--white);vertical-align:middle;margin-left:3px;}
  .services{color:var(--white);font-size:18px;display:flex;gap:20px;}
  .services span::before{content:"✓";font-weight:700;margin-right:4px;}
  .cta{font-family:"Ropa Sans",sans-serif;color:var(--white);font-size:32px;letter-spacing:.5px;}
  .info{color:var(--white);font-size:18px;}
  .web{color:var(--white);font-size:18px;display:flex;align-items:center;gap:6px;}
  .stamp{position:absolute;left:758px;top:14px;width:100px;height:78px;background:var(--stamp);}
  .address-line{position:absolute;left:586px;width:248px;height:2px;background:#111;}
</style>
</head>
<body>
<div class="sheet">

  <!-- Front -->
  <section class="card card--front">
    <svg class="shapes" width="862" height="575" viewBox="0 0 862 575">
      <defs>
        <linearGradient id="frontPhoto" x1="0" y1="0" x2="0" y2="1">
          <stop offset="0" stop-color="#9a9a96"/>
          <stop offset=".45" stop-color="#b8a58a"/>
          <stop offset=".7" stop-color="#6f6d68"/>
          <stop offset="1" stop-color="#55524d"/>
        </linearGradient>
      </defs>
      <rect width="862" height="575" fill="var(--white)"/>
      <rect y="85" width="862" height="4" fill="var(--sky)"/>
      <rect y="89" width="862" height="99" fill="var(--navy)"/>
      <rect y="188" width="862" height="118" fill="var(--blue)"/>
      <rect y="306" width="862" height="85" fill="var(--charcoal)"/>
      <rect y="391" width="862" height="61" fill="var(--blue)"/>
      <rect y="452" width="862" height="6" fill="var(--white)"/>
      <rect y="458" width="862" height="117" fill="var(--navy)"/>
      <circle cx="101" cy="291" r="349" fill="var(--white)" stroke="var(--sky)" stroke-width="5"/>
      <circle cx="101" cy="291" r="343" fill="url(#frontPhoto)" role="img" aria-label="Photo: uniformed technician giving a thumbs up in front of a freshly pressure-washed business entrance"/>
    </svg>
    <div class="t brand-name" style="left:621px;top:16px;">Riverbend Commercial</div>
    <div class="t brand-tag" style="left:621px;top:52px;">PRESSURE WASHING</div>
    <div class="t headline" style="left:638px;top:97px;font-size:38px;">KEEP YOUR</div>
    <div class="t headline" style="left:643px;top:137px;font-size:48px;">BUSINESS CLEAN</div>
    <p class="t body-copy" style="left:472px;top:193px;width:362px;margin:0;">We are able to remove gum and grease from concrete which is difficult for much of our competitors. We work for that need periodic pressure washing to keep clean.</p>
    <div class="t section-title" style="left:469px;top:314px;">We work in</div>
    <div class="t services" style="left:469px;top:350px;"><span>Sidewalks</span><span>Drive thrus</span><span>Dumpster pads</span></div>
    <p class="t body-copy" style="left:469px;top:398px;width:360px;margin:0;text-align:left;">We work at night when the businesses are closed or slow if 24hr.</p>
    <div class="t cta" style="left:433px;top:465px;">CALL US @ 12345678900</div>
    <div class="t info" style="left:437px;top:505px;">For more&nbsp; information&nbsp; please visit our website</div>
    <div class="t web" style="left:586px;top:528px;">
      <svg width="18" height="18" viewBox="0 0 18 18" aria-hidden="true"><circle cx="9" cy="9" r="7.5" fill="none" stroke="var(--sky)" stroke-width="1.4"/><ellipse cx="9" cy="9" rx="3.2" ry="7.5" fill="none" stroke="var(--sky)" stroke-width="1.2"/><path d="M1.5 9h15M3 5h12M3 13h12" stroke="var(--sky)" stroke-width="1.1"/></svg>
      www.companyname.com
    </div>
  </section>

  <!-- Back -->
  <section class="card card--back">
    <svg class="shapes" width="874" height="582" viewBox="0 0 874 582">
      <defs>
        <clipPath id="backPanel"><circle cx="172" cy="291" r="336"/></clipPath>
        <linearGradient id="backPhoto" x1="0" y1="0" x2="0" y2="1">
          <stop offset="0" stop-color="#a9aeb3"/>
          <stop offset=".45" stop-color="#8f97a6"/>
          <stop offset=".75" stop-color="#6b65a0"/>
          <stop offset="1" stop-color="#2e2a6e"/>
        </linearGradient>
      </defs>
      <rect width="874" height="582" fill="var(--white)"/>
      <circle cx="172" cy="291" r="340" fill="none" stroke="var(--sky)" stroke-width="5"/>
      <g clip-path="url(#backPanel)">
        <rect x="0" y="132" width="874" height="328" fill="url(#backPhoto)" role="img" aria-label="Photo: worker polishing a shiny commercial floor with an orange floor machine"/>
        <rect x="0" y="460" width="874" height="122" fill="var(--band)"/>
      </g>
    </svg>
    <div class="t brand-name" style="left:199px;top:48px;">Riverbend Commercial</div>
    <div class="t brand-tag" style="left:199px;top:84px;">PRESSURE WASHING</div>
    <div class="t section-title" style="left:22px;top:390px;">We work in</div>
    <div class="t services" style="left:22px;top:426px;gap:22px;"><span>Sidewalks</span><span>Drive thrus</span><span>Dumpster pads</span></div>
    <div class="t cta" style="left:10px;top:468px;">CALL US @ 12345678900</div>
    <div class="t info" style="left:15px;top:510px;">For more&nbsp; information&nbsp; please visit our website</div>
    <div class="t web" style="left:131px;top:533px;">
      <svg width="18" height="18" viewBox="0 0 18 18" aria-hidden="true"><circle cx="9" cy="9" r="7.5" fill="none" stroke="var(--navy)" stroke-width="1.4"/><ellipse cx="9" cy="9" rx="3.2" ry="7.5" fill="none" stroke="var(--navy)" stroke-width="1.2"/><path d="M1.5 9h15M3 5h12M3 13h12" stroke="var(--navy)" stroke-width="1.1"/></svg>
      www.companyname.com
    </div>
    <div class="stamp"></div>
    <div class="address-line" style="top:316px;"></div>
    <div class="address-line" style="top:339px;"></div>
    <div class="address-line" style="top:363px;"></div>
  </section>

</div>
</body>
</html>
```